Business Card for: Northbrook Financial Advisory Services Inc.

provide strategic financial advisory services to companies in the areas of corporate finance, mergers and acquisitions, executive coaching and strategic planning

Target Market(s)

Companies, banks, accountants, lawyers

Industry/Entity Type

High end business consulting in corporate finance, mergers and acquisitions, consulting

Contact Information for Business Card

Name of company, Name: xxxxxx xxxxxx , CEO, - phone number: 1-xxx-xxx-xxxx, - email address,

Requirements
Must have
• Must be professional and simple.
Nice to have
• simple, straight graphics, must give the impression that we are trustworthy, professional, competent
Should not have
• loud colors, loud design features

```html
<!DOCTYPE html>
<html lang="en">
<head>
<meta charset="utf-8">
<title>Northbrook Business Card</title>
<link href="https://fonts.googleapis.com/css2?family=Poppins:wght@400;500;600&display=swap" rel="stylesheet">
<style>
  :root {
    --backdrop: #dcdcdd;
    --navy: #0d238a;
    --paper: #ffffff;
    --ink: #111111;
  }
  * { box-sizing: border-box; margin: 0; padding: 0; }
  html, body { width: 679px; height: 1200px; overflow: hidden; }
  body {
    background: var(--backdrop);
    font-family: "Poppins", sans-serif;
    display: flex;
    flex-direction: column;
    align-items: center;
    justify-content: center;
    gap: 60px;
  }
  .card {
    width: 580px;
    height: 330px;
    position: relative;
  }
  .card-frame {
    position: absolute;
    inset: 24px;
  }
  .card--front { background: var(--navy); }
  .card--front .card-frame { border: 1px solid var(--paper); }
  .card--front .wordmark {
    position: absolute;
    inset: 0;
    display: flex;
    align-items: center;
    justify-content: center;
    color: var(--paper);
    font-weight: 600;
    font-size: 40px;
    letter-spacing: -1px;
  }
  .card--back { background: var(--paper); }
  .card--back .card-frame { border: 2px solid var(--navy); }
  .card-back-content {
    position: absolute;
    inset: 0;
    display: flex;
    align-items: center;
    padding-left: 84px;
    gap: 46px;
  }
  .card--back .wordmark {
    color: var(--navy);
    font-weight: 600;
    font-size: 31px;
    letter-spacing: -0.8px;
    width: 180px;
  }
  .contact-block { padding-top: 16px; }
  .contact-name {
    color: var(--navy);
    font-weight: 500;
    font-size: 19px;
    margin-bottom: 14px;
  }
  .contact-line {
    display: flex;
    align-items: center;
    gap: 4px;
    color: var(--ink);
    font-size: 11.5px;
    line-height: 21px;
  }
  .contact-line svg { width: 12px; height: 12px; fill: var(--ink); }
</style>
</head>
<body>
  <section class="card card--front">
    <div class="card-frame"></div>
    <div class="wordmark">northbrook</div>
  </section>

  <section class="card card--back">
    <div class="card-frame"></div>
    <div class="card-back-content">
      <div class="wordmark">northbrook</div>
      <div class="contact-block">
        <p class="contact-name">CEO NAME</p>
        <p class="contact-line">
          <svg viewBox="0 0 24 24" aria-hidden="true"><path d="M6.6 10.8a15.2 15.2 0 0 0 6.6 6.6l2.2-2.2c.3-.3.7-.4 1-.2 1.1.4 2.3.6 3.6.6.6 0 1 .4 1 1V20c0 .6-.4 1-1 1A17 17 0 0 1 3 4c0-.6.4-1 1-1h3.5c.6 0 1 .4 1 1 0 1.3.2 2.5.6 3.6.1.3 0 .7-.2 1z"/></svg>
          01632 960 480
        </p>
        <p class="contact-line">
          <svg viewBox="0 0 24 24" aria-hidden="true"><path d="M2 5h20v14H2zm2 2v.5l8 5 8-5V7l-8 5z"/></svg>
          talktous@northbrookservices.co.uk
        </p>
      </div>
    </div>
  </section>
</body>
</html>
```